Brennock transport business cards

Front of card, Looking for my logo on one side of the card

Back of card,
Brennock Transport Maintenance
Onsite Cars, Trucks & trailer maintenance and repairs
Gary Brennock
0452918406
Brennocktm@vexmail.test

```html
<!DOCTYPE html>
<html lang="en">
<head>
<meta charset="utf-8">
<title>Brennock Transport Maintenance – Business Cards</title>
<link rel="stylesheet" href="https://fonts.googleapis.com/css2?family=Alfa+Slab+One&family=Oswald:wght@400;500;600&display=swap">
<style>
  :root {
    --stage: #2a2a2c;
    --card-black: #0b0b0c;
    --card-black-soft: #161617;
    --white: #ffffff;
    --silver: #c9c9cc;
    --silver-dark: #8d8d92;
    --taupe: #9c8b89;
    --taupe-light: #b9aba8;
    --blue: #1a7fe0;
    --blue-dark: #0f3f7d;
    --ink: #121212;
  }
  * { margin: 0; padding: 0; box-sizing: border-box; }
  html, body { width: 1200px; height: 900px; overflow: hidden; }
  body {
    background: var(--stage);
    display: flex;
    flex-direction: column;
    align-items: center;
    justify-content: center;
    gap: 48px;
  }
  .card {
    position: relative;
    width: 630px;
    height: 360px;
    border-radius: 22px;
    overflow: hidden;
    background: radial-gradient(ellipse at 70% 20%, var(--card-black-soft), var(--card-black) 70%);
    box-shadow: 0 18px 40px rgba(0,0,0,.55);
  }

  /* wordmark */
  .wordmark { position: absolute; display: flex; flex-direction: column; align-items: flex-start; }
  .wordmark__name {
    font-family: "Alfa Slab One", serif;
    color: var(--white);
    font-size: 52px;
    line-height: 1;
    letter-spacing: 1px;
  }
  .wordmark__tagline {
    font-family: "Oswald", sans-serif;
    color: var(--white);
    font-size: 19px;
    letter-spacing: .5px;
    margin-top: 8px;
  }

  /* front card */
  .card--contact .wordmark { left: 150px; top: 54px; }
  .name-band {
    position: absolute; left: 0; right: 0; top: 176px; height: 56px;
    background: linear-gradient(90deg, var(--taupe) 0%, var(--taupe-light) 60%, var(--taupe) 100%);
    display: flex; align-items: center; justify-content: center;
  }
  .name-band__name {
    font-family: "Alfa Slab One", serif;
    font-size: 34px; letter-spacing: 2px; color: var(--ink);
  }
  .contact-row {
    position: absolute; left: 0; right: 0; top: 256px;
    display: flex; justify-content: center; gap: 40px;
  }
  .contact-item {
    display: flex; align-items: center; gap: 12px;
    font-family: "Oswald", sans-serif; font-size: 28px; color: var(--white);
  }
  .contact-item__icon { width: 34px; height: 34px; flex: none; }
  .edge-stripe {
    position: absolute; left: 0; right: 0; bottom: 0; height: 20px;
    background: linear-gradient(90deg, var(--blue-dark), var(--blue) 55%, var(--blue-dark));
  }

  /* back card */
  .card--service .wordmark { left: 150px; top: 46px; }
  .card--service .wordmark__name { color: var(--silver); }
  .card--service .wordmark__tagline { color: var(--silver-dark); }
  .big-phone {
    position: absolute; left: 150px; top: 150px;
    font-family: "Oswald", sans-serif; font-weight: 600;
    font-size: 66px; letter-spacing: 6px;
    color: var(--silver);
  }
  .service-band {
    position: absolute; left: 0; right: 0; bottom: 0; height: 92px;
    border-top: 5px solid var(--taupe-light);
    background: linear-gradient(90deg, var(--blue-dark), var(--blue) 55%, var(--blue-dark));
    display: flex; align-items: center; justify-content: center;
  }
  .service-band__text {
    font-family: "Oswald", sans-serif; font-weight: 500;
    font-size: 24px; color: var(--white); letter-spacing: .3px;
  }
</style>
</head>
<body>

  <section class="card card--contact" aria-label="Business card front">
    <div class="wordmark">
      <span class="wordmark__name">BRENNOCK</span>
      <span class="wordmark__tagline">TRANSPORT MAINTENANCE</span>
    </div>
    <div class="name-band"><span class="name-band__name">GARY BRENNOCK</span></div>
    <div class="contact-row">
      <div class="contact-item">
        <svg class="contact-item__icon" viewBox="0 0 34 34" aria-hidden="true">
          <circle cx="17" cy="17" r="17" fill="var(--blue)"/>
          <path d="M11 9c1-1 2.5-1 3 0l2 3c.5 1 0 2-1 2.5-.5.3-.5 1 0 2l2.5 2.5c1 .5 1.7.5 2 0 .5-1 1.5-1.5 2.5-1l3 2c1 .5 1 2 0 3-2 2-5 2-9-2s-6-8-5-12z" fill="#fff"/>
        </svg>
        <span>0452918406</span>
      </div>
      <div class="contact-item">
        <svg class="contact-item__icon" viewBox="0 0 34 34" aria-hidden="true">
          <circle cx="17" cy="17" r="17" fill="var(--blue)"/>
          <rect x="8" y="11" width="18" height="12" rx="1" fill="#fff"/>
          <path d="M8 11l9 7 9-7" fill="none" stroke="var(--blue)" stroke-width="1.6"/>
        </svg>
        <span>BRENNOCKTM@VEXMAIL.TEST</span>
      </div>
    </div>
    <div class="edge-stripe"></div>
  </section>

  <section class="card card--service" aria-label="Business card back">
    <div class="wordmark">
      <span class="wordmark__name">BRENNOCK</span>
      <span class="wordmark__tagline">TRANSPORT MAINTENANCE</span>
    </div>
    <div class="big-phone">0452918406</div>
    <div class="service-band">
      <span class="service-band__text">ONSITE CARS, TRUCKS &amp; TRAILER MAINTENANCE AND REPAIRS</span>
    </div>
  </section>

</body>
</html>
```